Web Design Project - vR Advisory

We want to modernise our web page profile. We have an existing web site that we are particularly not proud of (www.vradvisory.com.au).
We have started to build a new web site using Joomla and we like the structure of it, but we need it to be professionally designed and implemented.

This current development site can be viewed here: dev.vradvisory.com.au

We would like a complete design for the entire website, ready for deployment.

(We still need to finalise the content, as we have just developed new products that we hope to launch in August both on this web site and by a Partner Summit.)
Updates

Target Market(s)

Larger companies where the robustness of their IT infrastructure is critical. Our tools and services provide for monitoring of every device

Industry/Entity Type

Build

Requirements
Must have
• Responsive design for different screen sizes.

BrightDesk help desk software integrated with the website.
Currently can be viewed at support.vradvisory.com.au
Brightdesk only supports custom css.

Nice to have
• Customer experience testimonials in a rotating banner
(plain square) and (plain square) links in the footer
We use Avenir as a company font.
Use company colours as in the logo (green and blue)

```html
<!DOCTYPE html>
<html lang="en">
<head>
<meta charset="utf-8">
<title>vR Advisory – Home</title>
<link href="https://fonts.googleapis.com/css2?family=Nunito+Sans:wght@400;600;700;800&family=Arimo:wght@400;700&display=swap" rel="stylesheet">
<style>
:root{
  --green:#7aa83a;
  --green-dark:#5f8a26;
  --blue:#1a8cc4;
  --blue-deep:#0f78b0;
  --hero-a:#0b7fbd;
  --hero-b:#28a6dc;
  --ink:#222;
  --grey:#666;
  --page:#f4f4f4;
  --card:#e2e2e2;
  --footer:#1e1e22;
  --footer-field:#2c2c30;
  --footer-bar:#141416;
  --footer-text:#8a8a8a;
  --white:#fff;
}
*{margin:0;padding:0;box-sizing:border-box}
html,body{width:898px;height:1200px;overflow:hidden}
body{background:var(--page);font-family:"Nunito Sans",sans-serif;color:var(--ink);position:relative}
.abs{position:absolute}

.topline{left:0;top:0;width:898px;height:3px;background:#ccc}
.notice-bar{left:64px;top:0;width:770px;height:24px;background:var(--green);color:var(--white);font-size:9px;display:flex;align-items:center;justify-content:space-between;padding:0 10px}
.socials{display:flex;align-items:center;gap:4px;font-size:8px;letter-spacing:.3px}
.socials span.sq{width:14px;height:14px;background:var(--white);display:inline-block;margin-left:3px}

.brand{left:76px;top:44px;display:flex;align-items:center;gap:8px}
.brand .mark{width:40px;height:40px;border-radius:50%;background:var(--green)}
.brand .name{font-size:20px;font-weight:800;color:var(--blue)}
.main-nav{right:64px;top:62px;display:flex;gap:26px;font-size:11.5px}
.main-nav a{color:var(--ink);text-decoration:none}
.main-nav a.active{color:var(--blue)}

.hero{left:0;top:114px;width:898px;height:242px;background:linear-gradient(180deg,var(--hero-a),var(--hero-b))}
.hero h1{position:absolute;left:64px;top:48px;color:var(--white);font-size:37px;font-weight:800;line-height:45px}
.hero p{position:absolute;left:64px;top:142px;color:var(--white);font-size:19px;line-height:23px;width:420px}
.hero .devices{position:absolute;left:508px;top:28px;width:330px;height:184px;border-radius:6px;background:linear-gradient(180deg,#2a2f36,#cfd6dc)}

.section-title{width:898px;text-align:center;color:var(--blue);font-weight:800}
.services-title{top:374px;font-size:35px}
.card{top:431px;width:246px;height:153px;background:var(--card);box-shadow:0 8px 8px -6px rgba(0,0,0,.3);text-align:center;padding:10px 12px 0}
.card svg{display:block;margin:0 auto}
.card h3{font-size:19px;font-weight:700;margin:4px 0 6px;color:#333}
.card p{font-size:9.5px;line-height:11.5px;color:#555}
.card a{display:block;margin-top:5px;font-size:11.5px;font-weight:700;color:var(--blue);text-decoration:none}

.welcome{top:612px;width:898px;text-align:center;font-size:20px;color:#333}
.welcome b{font-size:38px;font-weight:800;color:var(--blue);margin-left:6px;vertical-align:-4px}
.taglines{top:668px;width:898px;text-align:center;color:var(--blue);font-size:14.5px;font-weight:600;line-height:20px}
.intro{left:100px;top:710px;width:698px;text-align:center;font-size:14px;line-height:17.5px;color:#222}
.intro p+p{margin-top:5px}

.clients-title{top:830px;font-size:24px;font-weight:400}
.clients{left:64px;top:866px;width:770px;height:46px;display:flex;align-items:center;justify-content:space-between}
.clients .client{font-size:19px;font-weight:700;color:#3a3a3a;display:flex;align-items:center;gap:5px}
.client .dot{width:14px;height:14px;background:#3a3a3a}

.footer{left:0;top:938px;width:898px;height:230px;background:var(--footer);font-family:"Arimo",sans-serif}
.footer h4{position:absolute;font-size:13px;font-weight:400;color:#e8e8e8;font-family:"Nunito Sans",sans-serif}
.gallery-text{position:absolute;left:64px;top:40px;width:220px;font-size:8.5px;line-height:11px;color:var(--footer-text)}
.gallery{position:absolute;left:64px;top:74px;display:grid;grid-template-columns:repeat(4,49px);gap:4px}
.gallery span{width:49px;height:48px;background:linear-gradient(135deg,#5a5a5e,#3a3a3e)}
.gallery span.lit{background:linear-gradient(135deg,#c9b79c,#8c7a66);outline:1px solid #ddd}
.field{position:absolute;left:377px;width:142px;background:var(--footer-field);border:1px solid #333;border-radius:2px;color:#ccc;font-size:7.5px;padding:6px 5px}
.send{position:absolute;left:436px;top:178px;width:83px;height:20px;background:var(--footer-field);border-radius:2px;color:#ddd;font-size:9px;text-align:center;line-height:20px}
.post{position:absolute;left:658px;width:176px;display:flex;gap:5px;border-bottom:1px solid #2e2e32;padding-bottom:6px}
.post .thumb{width:62px;height:44px;flex:none;background:linear-gradient(135deg,#d9dde2,#6d737b)}
.post b{display:block;font-weight:400;color:#2ea3e0;font-size:9px}
.post p{font-size:7.5px;line-height:11px;color:#777}

.bottom-bar{left:0;top:1168px;width:898px;height:32px;background:var(--footer-bar);font-family:"Arimo",sans-serif;font-size:8px;color:#ddd}
.bottom-bar .copy{position:absolute;left:64px;top:12px}
.bottom-nav{position:absolute;right:64px;top:11px;display:flex;gap:21px;font-size:9px}
.bottom-nav a{color:#bbb;text-decoration:none}
.bottom-nav a.active{color:#2ea3e0}
</style>
</head>
<body>
<div class="abs topline"></div>
<div class="abs notice-bar">
  <span>This is a notification bar. You can use it to post your proms and discounts.</span>
  <span class="socials">SOCIALIZE WITH US <span class="sq"></span><span class="sq"></span></span>
</div>

<div class="abs brand"><span class="mark"></span><span class="name">vR Advisory</span></div>
<nav class="abs main-nav">
  <a class="active" href="#">Home</a><a href="#">Services</a><a href="#">Support</a><a href="#">Products</a><a href="#">About Us</a><a href="#">Contact Us</a>
</nav>

<section class="abs hero">
  <h1>Any Device,<br>any Platform, anywhere</h1>
  <p>Cross-domain, performance and service level monitoring and management</p>
  <div class="devices" role="img" aria-label="Tablet, laptop, desktop and phone showing a monitoring dashboard"></div>
</section>

<h2 class="abs section-title services-title">Services</h2>

<div class="abs card" style="left:64px">
  <svg width="34" height="34" viewBox="0 0 34 34" fill="none" stroke="#7aa83a" stroke-width="2"><path d="M17 4a13 12 0 1 1-8 21l-5 3 2-6A13 12 0 0 1 17 4z"/><circle cx="11" cy="16" r="1" fill="#7aa83a"/><circle cx="17" cy="16" r="1" fill="#7aa83a"/><circle cx="23" cy="16" r="1" fill="#7aa83a"/></svg>
  <h3>Consulting Services</h3>
  <p>Lorem ipsum dolor sit amet, consectetur adipiscing elit. Nulla non est neque. Aliquam erat volutpat. Ut tristique odio sit amet nibh tincidunt, a imperdiet libero lobortis. Mauris mauris leo</p>
  <a href="#">Read More</a>
</div>
<div class="abs card" style="left:325px">
  <svg width="34" height="34" viewBox="0 0 34 34" fill="none" stroke="#7aa83a" stroke-width="2"><circle cx="17" cy="11" r="6"/><path d="M5 30c1-7 6-10 12-10s11 3 12 10z"/></svg>
  <h3>Professional Services</h3>
  <p>Lorem ipsum dolor sit amet, consectetur adipiscing elit. Nulla non est neque. Aliquam erat volutpat. Ut tristique odio sit amet nibh tincidunt, a imperdiet libero lobortis. Mauris mauris leo</p>
  <a href="#">Read More</a>
</div>
<div class="abs card" style="left:587px">
  <svg width="34" height="34" viewBox="0 0 34 34" fill="none" stroke="#7aa83a" stroke-width="2"><circle cx="17" cy="17" r="11" stroke-dasharray="5 3"/><circle cx="17" cy="17" r="7"/><circle cx="17" cy="17" r="3"/></svg>
  <h3>Productised Services</h3>
  <p>Lorem ipsum dolor sit amet, consectetur adipiscing elit. Nulla non est neque. Aliquam erat volutpat. Ut tristique odio sit amet nibh tincidunt, a imperdiet libero lobortis. Mauris mauris leo</p>
  <a href="#">Read More</a>
</div>

<div class="abs welcome">Welcome to <b>vR Advisory</b></div>
<div class="abs taglines">… delivers insight &amp; management into EVERY layer of Virtual and Physical infrastructure<br>… dedicated to making business sense of IT challenges</div>
<div class="abs intro">
  <p>We are an organisation that prides itself on attracting, employing, retaining and developing subject matter experts in the field of consulting, architecture and delivery.</p>
  <p>We employ the best to ensure that we deliver the best. Our extensive experience and expertise fuels the architecture and delivery practices, ensuring that what we propose to our customers<br>we also deploy, manage and support.</p>
</div>

<h2 class="abs section-title clients-title">Our Clients</h2>
<div class="abs clients">
  <svg width="20" height="28" viewBox="0 0 20 28"><path d="M16 3L5 14l11 11" fill="none" stroke="#333" stroke-width="4"/></svg>
  <span class="client">Stratalink</span>
  <span class="client"><span class="dot"></span>Paymesh</span>
  <span class="client">Norvex</span>
  <span class="client">Harbourline Telecom</span>
  <span class="client">Primeledger</span>
  <svg width="20" height="28" viewBox="0 0 20 28"><path d="M4 3l11 11L4 25" fill="none" stroke="#333" stroke-width="4"/></svg>
</div>

<footer class="abs footer">
  <h4 style="left:64px;top:18px">PHOTO GALLERY</h4>
  <p class="gallery-text">Lorem ipsum dolor sit amet, consectetur adipiscing elit. Nulla non est neque. Aliquam erat volutpat.</p>
  <div class="gallery" role="img" aria-label="Gallery of office and team photos">
    <span></span><span></span><span></span><span></span>
    <span></span><span class="lit"></span><span></span><span></span>
  </div>

  <h4 style="left:377px;top:20px">REQUEST A QUOTE</h4>
  <div class="field" style="top:44px;height:22px"><b>Name</b> (required)</div>
  <div class="field" style="top:70px;height:22px"><b>Email</b> (required)</div>
  <div class="field" style="top:96px;height:74px"><b>Message</b> (required)</div>
  <div class="send">Send Message</div>

  <h4 style="left:658px;top:18px">LATEST POSTS</h4>
  <div class="post" style="top:40px"><div class="thumb" role="img" aria-label="Business meeting photo"></div><div><b>This is a sample Post 1</b><p>Lorem ipsum dolor sit amet, consectetuer adipiscing elit, sed diam nonummy nibh...</p></div></div>
  <div class="post" style="top:104px"><div class="thumb" role="img" aria-label="Team at work photo"></div><div><b>This is a sample Post 2</b><p>Lorem ipsum dolor sit amet, consectetuer adipiscing elit, sed diam nonummy nibh...</p></div></div>
  <div class="post" style="top:168px;border:none"><div class="thumb" role="img" aria-label="Colleagues reviewing documents photo"></div><div><b>This is a sample Post 3</b><p>Lorem ipsum dolor sit amet, consectetuer adipiscing elit, sed diam nonummy nibh...</p></div></div>
</footer>

<div class="abs bottom-bar">
  <span class="copy">Copyright vR Advisory - 2013</span>
  <nav class="bottom-nav">
    <a class="active" href="#">Home</a><a href="#">Services</a><a href="#">Support</a><a href="#">Products</a><a href="#">About Us</a><a href="#">Contact Us</a>
  </nav>
</div>
</body>
</html>
```